Business Card Re-Design/Update

We'd like to update out business cards. I've included our current "Style guide" which has the colour scheme of the organisation in it. I've also included the branding files with logos etc in them.

I've also included a copy of one of our existing cards so that you can see how ugly/dated they look. I'd like a fresh modern corporate look.

Target Market(s)

These are for our clients, potential clients, industry contacts - like all business cards

Contact Information for Business Card

Name
Position
Company Address - Level 1, 47 Garnet Lane, Toowong Qld 4066
Direct Phone
mobile
Email
Website -www.korvalnet.com.au
Logo

Colors

Designer to choose colors to be used in the design.

Requirements
Must have
• Main Logo
• Cards will need to be editable to be able to personalize them for each new employee.
Nice to have
• The MapOUT, HandOVER, UpKEEP would be okay to have if they can be sensibly and professionally added to the look without detracting from the main imagery.
• Maybe they could go on the back of the card? will leave this to your creative discretion as to whether/where they fit.
Should not have
• Should not have decorative or script fonts

```html
<!DOCTYPE html>
<html lang="en">
<head>
<meta charset="utf-8">
<title>Korvalnet Business Card</title>
<link href="https://fonts.googleapis.com/css2?family=Arimo:wght@400;700&display=swap" rel="stylesheet">
<style>
  :root {
    --brand-red: #d71920;
    --ink-dark: #3a3a3a;
    --ink-grey: #6b6b6b;
    --paper: #ffffff;
    --canvas: #ffffff;
  }
  html, body {
    margin: 0;
    padding: 0;
    width: 1200px;
    height: 1000px;
    overflow: hidden;
    background: var(--canvas);
    font-family: "Arimo", Arial, sans-serif;
  }
  .canvas { position: relative; width: 1200px; height: 1000px; }
  .card {
    position: absolute;
    top: 324px;
    width: 563px;
    height: 352px;
    overflow: hidden;
    box-shadow: 0 3px 10px rgba(0,0,0,0.12);
  }
  .card--front { left: 25px; background: var(--paper); }
  .card--back { left: 612px; background: var(--brand-red); }

  .card__graphic { position: absolute; inset: 0; }

  .wordmark {
    position: absolute;
    display: flex;
    align-items: center;
    gap: 10px;
    line-height: 1;
    white-space: nowrap;
  }
  .wordmark__square { display: block; }
  .wordmark--front { left: 40px; top: 46px; font-size: 40px; color: var(--ink-dark); }
  .wordmark--front .wordmark__square { width: 40px; height: 40px; background: var(--brand-red); }
  .wordmark--back { left: 320px; top: 281px; font-size: 29px; color: var(--paper); }
  .wordmark--back .wordmark__square { width: 28px; height: 28px; background: var(--paper); }

  .contact { position: absolute; left: 47px; top: 114px; color: var(--ink-grey); }
  .contact__name { margin: 0; font-size: 22px; font-weight: 700; color: var(--ink-dark); line-height: 1; }
  .contact__surname { color: var(--brand-red); }
  .contact__line { margin: 0; font-size: 15px; line-height: 21px; }
  .contact__role { margin-top: 6px; }
  .contact__phones { position: absolute; left: 47px; top: 218px; color: var(--ink-grey); }
  .contact__web { position: absolute; left: 47px; top: 289px; color: var(--ink-grey); }
</style>
</head>
<body>
<main class="canvas">
  <section class="card card--front" aria-label="Card front">
    <svg class="card__graphic" width="563" height="352" viewBox="0 0 563 352" role="img" aria-label="Large red brand graphic area">
      <polygon points="227,258 455,0 563,0 563,352 310,352" fill="var(--brand-red)"/>
    </svg>
    <div class="wordmark wordmark--front">
      <span class="wordmark__square"></span>
      <span class="wordmark__name">korvalnet</span>
    </div>
    <div class="contact">
      <p class="contact__name">Maren <span class="contact__surname">Holt</span></p>
      <p class="contact__line contact__role">Business Development Manager</p>
      <p class="contact__line">mholt@korvalnet.com.au</p>
    </div>
    <div class="contact__phones">
      <p class="contact__line">+61 (0)412 555 019</p>
      <p class="contact__line">+61 (0)7 3555 0142</p>
    </div>
    <p class="contact__line contact__web">www.korvalnet.com.au</p>
  </section>

  <section class="card card--back" aria-label="Card back">
    <div class="wordmark wordmark--back">
      <span class="wordmark__square"></span>
      <span class="wordmark__name">korvalnet</span>
    </div>
  </section>
</main>
</body>
</html>
```